Restaurant service company needs a website!

I am looking for a skilled web designer/developer to create a professional, responsive, and easy-to-navigate website for my company, which specializes in servicing restaurant cooking equipment. The site should communicate trust, reliability, and technical expertise to our target audience, restaurant owners, managers, and commercial kitchen operators. I have included the company logos, if any other format for them is needed please let me know.

Target Market(s)

restaurant owners, managers, and commercial kitchen operators

Industry/Entity Type

Commercial Kitchen Equipment Service

Coding

Coded - Design and coding required

Number of Pages Required

1 page

Font styles to use
Serif
Sans Serif

Requirements
Must have
• Contact and service request forms, Click-to-call functionality for mobile, Clean, modern layout with strong visuals, Easy navigation, mobile-friendly
Nice to have
• Testimonials or Reviews, If possible a click-to-text functionality for mobile.
Should not have
• Any mention of Refrigeration or HVAC, "Free Quotes"

```html
<!DOCTYPE html>
<html lang="en">
<head>
<meta charset="utf-8">
<title>Ironline Kitchen Service</title>
<link href="https://fonts.googleapis.com/css2?family=Poppins:wght@300;400;500;600;700&family=Roboto:wght@400;500;700&display=swap" rel="stylesheet">
<style>
:root{
  --teal:#0f6680;
  --teal-dark:#0b5368;
  --yellow:#f6c445;
  --ink:#222;
  --muted:#666;
  --line:#d9d9d9;
  --white:#fff;
}
*{box-sizing:border-box;margin:0;padding:0}
html,body{width:1200px;height:4812px;overflow:hidden}
body{font-family:"Roboto",Arial,sans-serif;color:var(--ink);background:var(--white);position:relative}
.abs{position:absolute}
h1,h2,h3{font-family:"Poppins",Arial,sans-serif}
.btn{display:inline-flex;align-items:center;justify-content:center;gap:8px;font-family:"Roboto",sans-serif;font-weight:700;font-size:14px;border-radius:4px;height:36px;padding:0 16px;white-space:nowrap}
.btn-teal{background:var(--teal);color:#fff}
.btn-yellow{background:var(--yellow);color:#fff}
.btn-outline{border:1.5px solid #fff;color:#fff;font-weight:500;height:34px;font-size:13px;border-radius:2px}

/* header */
.site-header{top:0;left:0;width:1200px;height:94px;background:#fff}
.brand{left:165px;top:24px;display:flex;align-items:center;gap:10px}
.brand-box{width:28px;height:28px;border:2.5px solid var(--teal)}
.brand-name{font-family:"Poppins",sans-serif;font-weight:700;font-size:22px;color:var(--teal);letter-spacing:1px}
.main-nav{left:444px;top:38px;display:flex;gap:17px;font-size:13.5px;color:#333}
.call-pill{left:890px;top:32px;height:36px;width:150px;background:var(--teal);border-radius:6px;color:#fff;display:flex;align-items:center;padding-left:42px}
.call-pill .ring{position:absolute;left:-2px;top:-2px;width:40px;height:40px;border-radius:50%;background:#fff;border:2px solid var(--teal);display:flex;align-items:center;justify-content:center}
.call-pill small{display:block;font-size:8px;font-weight:700}
.call-pill b{font-size:14px}

/* hero */
.hero{top:94px;left:0;width:1200px;height:581px;background:linear-gradient(135deg,#7fb1bd 0%,#4e8c9c 55%,#3c7888 100%)}
.hero-title{left:162px;top:170px;font-size:46px;line-height:52px;font-weight:600;color:#fff;letter-spacing:-.3px}
.hero-sub{left:162px;top:345px;width:470px;font-size:17px;line-height:25px;color:#fff}
.hero-actions{left:162px;top:424px;display:flex;gap:16px}
.scroll-cue{left:589px;top:500px}
.quote-card{left:700px;top:120px;width:352px;height:525px;background:#fff;border-radius:24px;padding:24px 28px}
.quote-head{border-left:4px solid var(--teal);padding-left:10px;margin:6px 0 22px 16px}
.quote-head span{font-size:14px;font-weight:500;display:block}
.quote-head strong{font-family:"Poppins",sans-serif;font-size:20px;font-weight:600;color:#111}
.field{height:36px;border:1px solid #e1e1e1;border-radius:4px;margin-bottom:13px;font-size:11px;color:#888;padding:11px 14px;box-shadow:0 1px 2px rgba(0,0,0,.06)}
.field.area{height:104px}
.quote-card .btn{width:100%;height:42px;margin-top:6px;font-size:14px}

/* section headings */
.sec-title{width:1200px;left:0;text-align:center;font-family:"Poppins",sans-serif;font-size:36px;font-weight:300;color:#333}
.sec-title b{font-weight:500}
.sec-lead{left:330px;width:540px;text-align:center;font-size:13px;line-height:20px;color:#666}

/* services */
.service{width:278px;height:205px;border:4px solid #eee;background:#fff;text-align:center;padding-top:30px}
.service svg{height:40px}
.service h3{font-family:"Roboto",sans-serif;font-size:13.5px;font-weight:500;margin:12px 0 10px}
.service p{font-size:10.5px;line-height:15px;color:#666;padding:0 24px}

/* band */
.band{top:1400px;left:0;width:1200px;height:140px;background:var(--teal)}
.band p{position:absolute;left:174px;top:40px;width:660px;font-size:22px;line-height:31px;font-weight:500;color:#fff}
.band .btn{position:absolute;left:892px;top:51px}

/* about */
.about-photo{left:162px;top:1600px;width:438px;height:545px;border-radius:18px;background:linear-gradient(160deg,#b8b3aa,#8b867f 50%,#c9c3b6)}
.about-inset{left:386px;top:1924px;width:216px;height:213px;border:6px solid #fff;border-radius:16px;background:linear-gradient(160deg,#cfd4d6,#8e979b)}
.eyebrow{left:630px;top:1628px;font-size:12px;font-weight:500;color:var(--teal)}
.about-title{left:630px;top:1650px;width:420px;font-size:29px;line-height:41px;font-weight:400;color:#222}
.about-text{left:630px;top:1826px;width:400px;font-size:12.5px;line-height:19px;color:#555}
.about-call{left:626px;top:1944px;display:flex;gap:14px;align-items:center;font-size:12.5px;line-height:18px}
.about-call .ic{width:44px;height:40px;background:var(--teal);border-radius:6px;display:flex;align-items:center;justify-content:center}
.about-note{left:632px;top:2015px;font-size:13px;line-height:20px;width:330px}
.about-actions{left:626px;top:2088px;display:flex;gap:16px}

/* banner */
.banner{top:2245px;left:0;width:1200px;height:493px;background:linear-gradient(120deg,#9bbcc4,#6d98a4 50%,#87aab3)}
.banner h2{position:absolute;left:162px;top:183px;width:650px;font-size:37px;line-height:39px;font-weight:500;color:#fff}
.banner .btn{position:absolute;left:162px;top:327px}
.play{left:944px;top:365px;width:82px;height:82px;border-radius:50%;background:var(--yellow)}

/* gallery */
.tile{width:284px;height:288px}

/* testimonial */
.testimonials{top:3580px;left:0;width:1200px;height:325px;background:var(--teal)}
.t-frame{left:160px;top:60px;width:880px;height:210px;border:1.5px solid rgba(255,255,255,.7)}
.t-body{left:220px;top:145px;width:760px;text-align:center;color:#fff;font-size:14.5px;line-height:20px}
.t-name{left:0;width:1200px;top:247px;text-align:center;color:#fff;font-size:13px;font-weight:500}
.t-role{left:0;width:1200px;top:266px;text-align:center;color:#fff;font-size:11px}
.stars{left:550px;top:80px}

/* faq */
.faq-q{width:370px;height:52px;border-bottom:1px solid var(--line);font-size:12.5px;display:flex;justify-content:space-between;align-items:center;padding:0 4px}
.faq-a{width:360px;font-size:11px;line-height:19px;color:#555}

/* cta & footer */
.footer{top:4330px;left:0;width:1200px;height:482px;background:var(--teal)}
.cta-card{left:84px;top:4330px;width:1008px;height:190px;background:#fff;border-radius:0 0 24px 24px}
.cta-title{left:162px;top:4356px;font-size:38px;line-height:48px;font-weight:400;color:#222}
.cta-actions{left:736px;top:4392px;display:flex;gap:18px}
.foot-brand{left:182px;top:4670px;color:#fff;font-family:"Poppins",sans-serif;font-weight:600;font-size:27px;letter-spacing:2px}
.foot-brand small{display:block;font-size:12px;letter-spacing:5px;font-weight:500;text-align:center}
.foot-mark{left:232px;top:4530px;width:110px;height:110px;border:4px solid #fff}
.foot-col{color:#fff;font-size:13px;line-height:24px}
.foot-col h4{font-family:"Roboto",sans-serif;font-size:14px;font-weight:500;margin-bottom:12px}
.socials{display:flex;gap:8px;margin-top:10px}
.socials span{width:26px;height:26px;border-radius:50%;background:#fff}
.copyright{left:0;top:4762px;width:1200px;height:50px;border-top:1px solid rgba(255,255,255,.3);color:#fff;font-size:12px;padding:18px 168px}
</style>
</head>
<body>

<header class="site-header abs">
  <div class="brand abs"><span class="brand-box"></span><span class="brand-name">IRONLINE</span></div>
  <nav class="main-nav abs"><span>Home</span><span>About us</span><span>Services</span><span>Gallery</span><span>Testimonials</span><span>Contact us</span></nav>
  <div class="call-pill abs">
    <span class="ring"><svg width="20" height="20" viewBox="0 0 24 24"><path d="M6.6 10.8a15 15 0 0 0 6.6 6.6l2.2-2.2c.3-.3.7-.4 1-.2 1.1.4 2.3.6 3.6.6.6 0 1 .4 1 1V20c0 .6-.4 1-1 1A17 17 0 0 1 3 4c0-.6.4-1 1-1h3.5c.6 0 1 .4 1 1 0 1.3.2 2.5.6 3.6.1.3 0 .7-.2 1z" fill="#0f6680"/></svg></span>
    <div><small>CALL US TODAY</small><b>555-014-2290</b></div>
  </div>
</header>

<section class="hero abs" role="img" aria-label="Commercial kitchen with stainless steel equipment under a teal tint">
  <h1 class="hero-title abs">Commercial<br>Kitchen &amp; Restaurant<br>Equipment</h1>
  <p class="hero-sub abs">Helping restaurants stay cooking with expert equipment repair and preventative maintenance.</p>
  <div class="hero-actions abs">
    <span class="btn btn-teal"><svg width="14" height="14" viewBox="0 0 24 24"><path d="M6.6 10.8a15 15 0 0 0 6.6 6.6l2.2-2.2c.3-.3.7-.4 1-.2 1.1.4 2.3.6 3.6.6.6 0 1 .4 1 1V20c0 .6-.4 1-1 1A17 17 0 0 1 3 4c0-.6.4-1 1-1h3.5c.6 0 1 .4 1 1 0 1.3.2 2.5.6 3.6.1.3 0 .7-.2 1z" fill="#fff"/></svg>555-014-2290</span>
    <span class="btn btn-yellow" style="font-size:12px">REQUEST SERVICE</span>
  </div>
  <svg class="scroll-cue abs" width="22" height="60" viewBox="0 0 22 60"><rect x="1" y="1" width="20" height="32" rx="10" fill="none" stroke="#fff" stroke-width="2"/><rect x="9" y="8" width="4" height="8" rx="2" fill="#fff"/><path d="M6 40l5 5 5-5M6 50l5 5 5-5" stroke="#fff" stroke-width="1.5" fill="none"/></svg>
</section>

<form class="quote-card abs">
  <div class="quote-head"><span>looking for a Service</span><strong>BOOK A SERVICE VISIT</strong></div>
  <div class="field">First Name*</div>
  <div class="field">Last Name*</div>
  <div class="field">Phone*</div>
  <div class="field">Email*</div>
  <div class="field" style="text-align:center">-------- Select Services --------</div>
  <div class="field area">Message</div>
  <div class="btn btn-teal">REQUEST SERVICE</div>
</form>

<h2 class="sec-title abs" style="top:722px">OUR <b>SERVICES</b></h2>
<p class="sec-lead abs" style="top:774px">We understand how critical your kitchen is to your business — that's why we provide prompt response times, transparent pricing, and quality repairs that last</p>

<div class="service abs" style="left:162px;top:855px"><svg viewBox="0 0 72 40" width="72"><rect x="2" y="2" width="68" height="36" rx="3" fill="none" stroke="#0f6680" stroke-width="3"/><rect x="8" y="14" width="24" height="18" fill="#0f6680"/><rect x="40" y="14" width="24" height="18" fill="#0f6680"/><path d="M2 9h68" stroke="#0f6680" stroke-width="3"/></svg><h3>Oven &amp; Range</h3><p>The point of using Lorem Ipsum is that it has a more-or-less normal distribution of letters, as opposed to using</p></div>
<div class="service abs" style="left:472px;top:855px"><svg viewBox="0 0 40 40" width="40"><path d="M4 18h32a16 14 0 0 1-32 0z" fill="#0f6680"/><path d="M10 12c0-4 4-4 4-8M20 12c0-4 4-4 4-8M30 12c0-4 4-4 4-8" stroke="#0f6680" stroke-width="2" fill="none"/><path d="M12 30l-4 8M28 30l4 8" stroke="#0f6680" stroke-width="3"/></svg><h3>Grill &amp; Fryer Maintenance</h3><p>The point of using Lorem Ipsum is that it has a more-or-less normal distribution of letters, as opposed to using</p></div>
<div class="service abs" style="left:782px;top:855px"><svg viewBox="0 0 28 40" width="28"><rect x="2" y="2" width="24" height="36" rx="2" fill="#0f6680"/><path d="M2 15h24" stroke="#fff" stroke-width="2"/><rect x="18" y="6" width="3" height="6" fill="#fff"/><circle cx="14" cy="27" r="6" fill="none" stroke="#fff" stroke-width="2"/></svg><h3>Dishwasher &amp; Steamer Repair</h3><p>The point of using Lorem Ipsum is that it has a more-or-less normal distribution of letters, as opposed to using</p></div>
<div class="service abs" style="left:162px;top:1115px"><svg viewBox="0 0 56 40" width="56"><rect x="10" y="8" width="34" height="26" rx="3" fill="#0f6680"/><path d="M44 21h10M2 21h8" stroke="#0f6680" stroke-width="3" fill="none"/><path d="M30 14l-4 8h6l-4 8" stroke="#fff" stroke-width="2" fill="none"/></svg><h3>Gas &amp; Electrical Equipment</h3><p>The point of using Lorem Ipsum is that it has a more-or-less normal distribution of letters, as opposed to using</p></div>
<div class="service abs" style="left:472px;top:1115px"><svg viewBox="0 0 40 40" width="40"><path d="M20 2l16 6v12c0 9-7 15-16 18C11 35 4 29 4 20V8z" fill="none" stroke="#0f6680" stroke-width="3"/><circle cx="20" cy="19" r="6" fill="#0f6680"/><path d="M28 26l8 10h-16z" fill="#0f6680"/></svg><h3>Preventive Maintenance</h3><p>The point of using Lorem Ipsum is that it has a more-or-less normal distribution of letters, as opposed to using</p></div>
<div class="service abs" style="left:782px;top:1115px"><svg viewBox="0 0 40 40" width="40"><path d="M6 34L30 10M10 6l24 28" stroke="#0f6680" stroke-width="5" stroke-linecap="round"/><circle cx="32" cy="8" r="5" fill="none" stroke="#0f6680" stroke-width="3"/></svg><h3>Precise Installation</h3><p>The point of using Lorem Ipsum is that it has a more-or-less normal distribution of letters, as opposed to using</p></div>

<section class="band abs">
  <p>We specialize in fast, reliable commercial kitchen equipment service — because downtime isn't an option</p>
  <span class="btn btn-outline">Contact Us Today</span>
</section>

<div class="about-photo abs" role="img" aria-label="Chefs cooking beneath a rack of hanging pans"></div>
<div class="about-inset abs" role="img" aria-label="Stainless steel kitchen equipment line"></div>
<p class="eyebrow abs">Welcome To Ironline</p>
<h2 class="about-title abs">We are a team of certified technicians specializing in commercial kitchen equipment repair.</h2>
<p class="about-text abs">The point of using Lorem Ipsum is that it has a more-or-less normal distribution of letters, as opposed to using 'Content here, content here', making it look like readable English. Many desktop publishing packages and web page editors now use Lorem Ipsum as their default model text, and a search for 'lorem ipsum'</p>
<div class="about-call abs"><span class="ic"><svg width="22" height="22" viewBox="0 0 24 24"><path d="M6.6 10.8a15 15 0 0 0 6.6 6.6l2.2-2.2c.3-.3.7-.4 1-.2 1.1.4 2.3.6 3.6.6.6 0 1 .4 1 1V20c0 .6-.4 1-1 1A17 17 0 0 1 3 4c0-.6.4-1 1-1h3.5c.6 0 1 .4 1 1 0 1.3.2 2.5.6 3.6.1.3 0 .7-.2 1z" fill="#fff"/></svg></span><span>Have any question? Give us a call<br>+01 555-014-2290</span></div>
<p class="about-note abs">We know commercial kitchens — and we know how to keep them running at their best.</p>
<div class="about-actions abs"><span class="btn btn-teal">Explore Products</span><span class="btn btn-yellow">Request Service</span></div>

<section class="banner abs" role="img" aria-label="Wide commercial kitchen with pots and extraction hoods under a teal tint">
  <h2>Built on trust, powered by skill — we keep your kitchen working, so you can focus on what matters.</h2>
  <span class="btn btn-outline">Contact Us Today</span>
  <div class="play abs"><svg width="82" height="82" viewBox="0 0 82 82"><path d="M33 27l22 14-22 14z" fill="#0f6680"/></svg></div>
</section>

<h2 class="sec-title abs" style="top:2782px">OUR <b>GALLERY</b></h2>
<p class="sec-lead abs" style="top:2834px">We understand how critical your kitchen is to your business — that's why we provide prompt response times, transparent pricing, and quality repairs that last</p>
<div class="tile abs" style="left:160px;top:2912px;background:linear-gradient(160deg,#6f6757,#3a3833)" role="img" aria-label="Kitchen line with pots on the range"></div>
<div class="tile abs" style="left:458px;top:2912px;background:linear-gradient(160deg,#c9cfd2,#6e7579)" role="img" aria-label="Stainless steel pans on a cooktop"></div>
<div class="tile abs" style="left:756px;top:2912px;background:linear-gradient(160deg,#5b82a8,#2f4862)" role="img" aria-label="Steel cooking vessels in blue light"></div>
<div class="tile abs" style="left:160px;top:3218px;background:linear-gradient(160deg,#a0673a,#3c2a1c)" role="img" aria-label="Copper bowls on a kitchen counter"></div>
<div class="tile abs" style="left:458px;top:3218px;background:linear-gradient(160deg,#bfc6ca,#7d868b)" role="img" aria-label="Kitchen with steel pans and hoods"></div>
<div class="tile abs" style="left:756px;top:3218px;background:linear-gradient(160deg,#9aa3a9,#3f464b)" role="img" aria-label="Close view of steel cookware"></div>

<section class="testimonials abs">
  <div class="t-frame abs"></div>
  <svg class="abs" style="left:576px;top:22px" width="48" height="40" viewBox="0 0 48 40"><path d="M2 18C2 8 8 2 16 2v8c-4 0-6 3-6 8h10v20H2zM28 18c0-10 6-16 14-16v8c-4 0-6 3-6 8h10v20H28z" fill="#fff"/></svg>
  <svg class="stars abs" width="100" height="18" viewBox="0 0 100 18"><g fill="#f6c445"><path id="s" d="M9 1l2.4 5.3 5.6.5-4.3 3.8 1.3 5.6L9 13.2 4 16.2l1.3-5.6L1 6.8l5.6-.5z"/><use href="#s" x="20"/><use href="#s" x="40"/><use href="#s" x="60"/><use href="#s" x="80"/></g></svg>
  <p class="t-body abs">The point of using Lorem Ipsum is that it has a more-or-less normal distribution of letters, as opposed to using 'Content here, content here', making it look like readable English. Many desktop publishing packages and web page editors now use Lorem Ipsum as their default model text,</p>
  <p class="t-name abs">Dana R. Whitfield</p>
  <p class="t-role abs">Verified Clients</p>
  <svg class="abs" style="left:138px;top:150px" width="12" height="20" viewBox="0 0 12 20"><path d="M10 2L2 10l8 8" stroke="#fff" stroke-width="2" fill="none"/></svg>
  <svg class="abs" style="left:1046px;top:150px" width="12" height="20" viewBox="0 0 12 20"><path d="M2 2l8 8-8 8" stroke="#fff" stroke-width="2" fill="none"/></svg>
</section>

<h2 class="sec-title abs" style="top:3938px">FREQUENTLY <b>ASKED QUESTIONS</b></h2>
<div class="faq-q abs" style="left:162px;top:4018px"><span>1. What types of equipment do you service?</span><span>+</span></div>
<div class="faq-q abs" style="left:162px;top:4072px"><span>2. Do you offer emergency repair services?</span><span>+</span></div>
<div class="faq-q abs" style="left:162px;top:4132px;border:none"><span>3. Do you work with restaurants, or only large kitchens?</span><span>-</span></div>
<p class="faq-a abs" style="left:170px;top:4188px">The point of using Lorem Ipsum is that it has a more-or-less normal distribution of letters, as opposed to using 'Content here', making it look like readable English. Many desktop publishing packages and web page editors now use Lorem Ipsum as their default model text, and a search.</p>
<div class="faq-q abs" style="left:606px;top:4018px"><span>4. How do you charge for service calls?</span><span>+</span></div>
<div class="faq-q abs" style="left:606px;top:4072px"><span>5. Do you offer preventative maintenance plans?</span><span>+</span></div>
<div class="faq-q abs" style="left:606px;top:4126px;border:none"><span>6. Are your technicians certified?</span><span>-</span></div>
<p class="faq-a abs" style="left:612px;top:4180px">The point of using Lorem Ipsum is that it has a more-or-less normal distribution of letters, as opposed to using 'Content here', making it look like readable English. Many desktop publishing packages and web page editors now use Lorem Ipsum as their default model text, and a search.</p>

<footer class="footer abs"></footer>
<div class="cta-card abs"></div>
<h2 class="cta-title abs">Let's get Install<br>For your Kitchen Equipment</h2>
<div class="cta-actions abs"><span class="btn btn-teal">555-014-2290</span><span class="btn btn-yellow">Request Service</span></div>

<div class="foot-mark abs"></div>
<div class="foot-brand abs">IRONLINE<small>KITCHEN SERVICE</small></div>
<div class="foot-col abs" style="left:468px;top:4540px"><h4>Quick Link</h4>Home<br>About Us<br>Services<br>Gallery<br>Testimonials<br>Contact Us</div>
<div class="foot-col abs" style="left:636px;top:4536px"><h4>Our Services</h4>Oven &amp; Range<br>Grill &amp; Fryer Maintenance<br>Dishwasher &amp; Steamer Repair<br>Gas &amp; Electrical Equipment<br>Preventive Maintenance<br>Precise Installation</div>
<div class="foot-col abs" style="left:882px;top:4540px"><h4>Contact us</h4>
  <div style="display:flex;gap:8px"><svg width="12" height="16" viewBox="0 0 12 16" style="margin-top:4px"><path d="M6 0a6 6 0 0 1 6 6c0 4-6 10-6 10S0 10 0 6a6 6 0 0 1 6-6z" fill="#fff"/><circle cx="6" cy="6" r="2" fill="#0f6680"/></svg><span>812 Harbor Mill Road,<br>Cedar Point, FL 30000</span></div>
  <div style="display:flex;gap:8px;align-items:center;margin-top:4px"><svg width="13" height="10" viewBox="0 0 13 10"><rect width="13" height="10" fill="#fff"/><path d="M0 0l6.5 5L13 0" stroke="#0f6680" fill="none"/></svg>hello@ironlineservice.com</div>
  <div style="display:flex;gap:8px;align-items:center;margin-top:6px"><svg width="12" height="12" viewBox="0 0 24 24"><path d="M6.6 10.8a15 15 0 0 0 6.6 6.6l2.2-2.2c.3-.3.7-.4 1-.2 1.1.4 2.3.6 3.6.6.6 0 1 .4 1 1V20c0 .6-.4 1-1 1A17 17 0 0 1 3 4c0-.6.4-1 1-1h3.5c.6 0 1 .4 1 1 0 1.3.2 2.5.6 3.6.1.3 0 .7-.2 1z" fill="#fff"/></svg>555-014-2290</div>
  <div class="socials"><span></span><span></span><span></span></div>
</div>
<div class="copyright abs">© 2025 ironlineservice.com. All Rights Reserved</div>

</body>
</html>
```